Kelvora Power

We need a business card for "Kelvora power". I have uploaded the logo, the color of the card should be according to the logo "Blackish".
Basically kelvora power is a solar company.
Also we would like a sample file in which we can edit the information such names and contact details ourselves
The card would be two sided with following details
1- logo on front and underneath the logo there should be a line saying
"Cleaner . Cheaper . Power"
2-website i.e "www.kelvorapower.example"
3- Icons for Facebook and Instagram that tells the clients we are available on both social sites.
4- name of the person with his/her designation underneath and email address
5-contact number
6- 1-800--- number with the extension number

its up to the designer how he/she places the details,but it must look professional

5-contact number

Requirements
Must have
• 1- logo on front and underneath the logo there should be a line saying
• "Cleaner . Cheaper . Power"
• 2-website i.e "www.kelvorapower.example"
• 3- Icons for Facebook and Instagram that tells the clients we are available on both social sites.
• 4- name of the person with his/her designation underneath and email address
• 5-contact number of the person
• 6- 1-800--- number with the extension number
• 7-card should be in black shade like the logo

```html
<!DOCTYPE html>
<html lang="en">
<head>
<meta charset="utf-8">
<title>Kelvora Power – Business Card</title>
<link href="https://fonts.googleapis.com/css2?family=Jost:wght@400;500;600;700&display=swap" rel="stylesheet">
<style>
  :root{
    --page:#3a3a3c;
    --lime:#8dc63f;
    --lime-deep:#7fb236;
    --ink:#1b1d1f;
    --navy:#1f2833;
    --slate:#9ba1a8;
    --pale:#c9cdd2;
  }
  *{margin:0;padding:0;box-sizing:border-box}
  html,body{width:1200px;height:900px;overflow:hidden}
  body{background:var(--page);font-family:"Jost",sans-serif;position:relative}
  .card{position:absolute;top:302px;width:513px;height:295px;border-radius:22px;box-shadow:0 6px 14px rgba(0,0,0,.35)}
  .card-front{left:72px;background:var(--lime);color:var(--ink);text-align:center}
  .card-back{left:616px;background:var(--navy);color:var(--pale)}

  .front-brand{position:absolute;left:0;right:0;top:128px;font-weight:700;font-size:38px;line-height:1;letter-spacing:-.5px;color:var(--ink)}
  .front-tagline{position:absolute;left:0;right:0;top:212px;font-size:15px;letter-spacing:3px;font-weight:500}
  .front-web{position:absolute;left:0;right:0;top:258px;font-size:12.5px}

  .back-brand{position:absolute;left:32px;top:42px;display:flex;align-items:center;gap:12px}
  .back-brand .mark{width:26px;height:26px;border-radius:50%;background:var(--lime)}
  .back-brand .name{font-weight:700;font-size:28px;color:var(--lime);line-height:1}

  .person{position:absolute;left:44px;top:146px;right:28px}
  .person-name{font-size:18px;color:var(--lime);letter-spacing:.3px;font-weight:400}
  .person-role{display:flex;align-items:center;gap:10px;font-size:13.5px;font-weight:600;color:var(--slate);margin-top:2px}
  .person-role::after{content:"";flex:1;height:1px;background:var(--slate)}

  .contacts{position:absolute;left:44px;top:201px;list-style:none;font-size:13.5px;line-height:19px;color:var(--pale)}
  .contacts li{display:flex;align-items:center;gap:7px}
  .contacts .icon{width:10px;height:10px;border-radius:50%;background:var(--lime);flex:none}

  .address{position:absolute;left:327px;top:201px;font-size:13.5px;line-height:19px;color:var(--pale);font-style:normal}
  .social{display:flex;gap:4px;margin-top:5px}
  .social span{width:10px;height:10px;background:var(--pale);border-radius:2px}
</style>
</head>
<body>
  <section class="card card-front" aria-label="Card front">
    <div class="front-brand">Kelvora Power</div>
    <p class="front-tagline">CLEANER . CHEAPER . POWER</p>
    <p class="front-web">www.kelvorapower.example</p>
  </section>

  <section class="card card-back" aria-label="Card back">
    <div class="back-brand"><span class="mark"></span><span class="name">Kelvora Power</span></div>

    <div class="person">
      <h1 class="person-name">DANIEL MARLOWE</h1>
      <p class="person-role">managing director</p>
    </div>

    <ul class="contacts">
      <li><span class="icon"></span>5550 123 456</li>
      <li><span class="icon"></span>1 833 KVSOLAR</li>
      <li><span class="icon"></span>d.marlowe@kelvorapower.example</li>
      <li><span class="icon"></span>www.kelvorapower.example</li>
    </ul>

    <address class="address">
      14 Sunridge Commerce Rd.<br>
      Harlow Flats<br>
      K7P 2L4
      <div class="social" aria-label="Social profiles"><span></span><span></span></div>
    </address>
  </section>
</body>
</html>
```